Orchards Under Snow

A 3rd Volume of Poetry, dealing with Power, Politics, Love, and General topics. The major theme is the misuse of power across al the continents. I would like a background map of the world and a stylistic fire depicting symbolically each continent on fire. This can be abstract. The title may be included in the artwork. alone or in conjunction with the world map.

```html
<!DOCTYPE html>
<html lang="en">
<head>
<meta charset="utf-8">
<title>Orchards Under Snow — Poetry: Volume III</title>
<link rel="stylesheet" href="https://fonts.googleapis.com/css2?family=League+Gothic&family=Allura&family=Marcellus&family=Raleway:wght@500&display=swap">
<style>
  :root {
    --ember-red: #c23a2a;
    --deep-crimson: #7a2430;
    --dusk-violet: #3e2c5c;
    --flame-gold: #f0a42a;
    --flame-orange: #e0601c;
    --title-cream: #fbf1a6;
    --title-shadow: #2f1a1e;
    --script-red: #e2401c;
    --band-plum: #43263c;
    --band-text: #f3e6c4;
  }
  html, body {
    margin: 0;
    padding: 0;
    width: 1200px;
    height: 636px;
    overflow: hidden;
    background: #ffffff;
  }
  .cover {
    position: relative;
    width: 1200px;
    height: 636px;
    overflow: hidden;
  }
  .cover__artwork {
    position: absolute;
    inset: 0;
    background:
      radial-gradient(ellipse 150px 210px at 780px 360px, rgba(240,164,42,0.85), rgba(224,96,28,0.4) 60%, transparent 100%),
      radial-gradient(ellipse 190px 90px at 700px 110px, rgba(240,164,42,0.7), transparent 100%),
      radial-gradient(ellipse 150px 130px at 150px 140px, rgba(224,96,28,0.75), transparent 100%),
      radial-gradient(ellipse 90px 140px at 260px 430px, rgba(200,90,30,0.7), transparent 100%),
      radial-gradient(ellipse 120px 110px at 1130px 470px, rgba(224,96,28,0.6), transparent 100%),
      radial-gradient(circle at 620px 330px, rgba(90,40,70,0.55), transparent 55%),
      linear-gradient(100deg, var(--ember-red) 0%, var(--deep-crimson) 45%, var(--dusk-violet) 100%);
  }
  .cover__title {
    position: absolute;
    left: 0;
    top: 0;
    width: 1200px;
    height: 420px;
  }
  .title-main {
    font-family: "League Gothic", "Oswald", sans-serif;
    fill: var(--title-cream);
  }
  .title-main--shadow { fill: var(--title-shadow); }
  .title-link {
    font-family: "Raleway", sans-serif;
    font-weight: 500;
    fill: var(--script-red);
  }
  .title-script {
    font-family: "Allura", cursive;
    fill: var(--script-red);
    stroke: var(--title-shadow);
    stroke-width: 1.5;
    paint-order: stroke;
  }
  .cover__author {
    position: absolute;
    left: 737px;
    top: 498px;
    margin: 0;
    font-family: "Marcellus", serif;
    font-size: 38px;
    letter-spacing: 0.5px;
    color: var(--title-cream);
    white-space: nowrap;
  }
  .cover__band {
    position: absolute;
    left: 7px;
    right: 0;
    top: 560px;
    height: 49px;
    background: var(--band-plum);
  }
  .cover__series {
    position: absolute;
    left: 780px;
    top: 0;
    margin: 0;
    line-height: 49px;
    font-family: "Marcellus", serif;
    font-size: 20px;
    color: var(--band-text);
    white-space: nowrap;
  }
</style>
</head>
<body>
  <main class="cover">
    <div class="cover__artwork" role="img" aria-label="World map with each continent stylised as burning flames over a swirling red and violet background"></div>

    <svg class="cover__title" viewBox="0 0 1200 420" aria-label="Orchards Under Snow">
      <text class="title-main title-main--shadow" x="679" y="170" font-size="190" textLength="487" lengthAdjust="spacingAndGlyphs">ORCHARDS</text>
      <text class="title-main" x="673" y="163" font-size="190" textLength="487" lengthAdjust="spacingAndGlyphs">ORCHARDS</text>
      <text class="title-link" x="748" y="198" font-size="22">under</text>
      <text class="title-script" x="800" y="360" font-size="200">Snow</text>
    </svg>

    <p class="cover__author">Harlan E. Voss</p>

    <div class="cover__band">
      <p class="cover__series">Poetry: Volume III</p>
    </div>
  </main>
</body>
</html>
```